Flyer design for guitar parts website

We are looking for an eye catching flyer design to include within our order packaging to persuade our Zubit and Kestrix customers to purchase from our website.

The flyer will be double sided, with one side offering buyers a discount for shopping on our website, and the other side advertising our loyalty points scheme, and the benefits the company it.

We've attached our company logo and our loyalty points logo.

I've also attached a banner design we used recently for our rewards program.

Target Market(s)

Males, aged 20 to 65

Colors
f68e4d
f04a51
886aae
3377b5

Requirements
Must have
• The flyer will be A6 size
• The focus of the front must be on the 20% discount for first order.
• The web address must also be prominent, as must our logo
• There will also be a discount code displayed.
• The back fo the flyer will contain the loyalyt points logo, and information about how the points work, and how they can be redeemed

```html
<!DOCTYPE html>
<html lang="en">
<head>
<meta charset="utf-8">
<title>Surprice Sale Flyer</title>
<link rel="stylesheet" href="https://fonts.googleapis.com/css2?family=Oswald:wght@300;400;500&family=Montserrat:wght@700;800&family=Open+Sans:wght@400;600&display=swap">
<style>
  :root {
    --backdrop: #606060;
    --paper: #ffffff;
    --ink: #222222;
    --accent-red: #ec1c3a;
    --footer-bg: #2a2a2a;
    --light-text: #ffffff;
  }
  * { margin: 0; padding: 0; box-sizing: border-box; }
  html, body {
    width: 1200px; height: 877px; overflow: hidden;
    background: var(--backdrop);
  }
  .flyer {
    position: absolute; left: 314px; top: 35px;
    width: 570px; height: 808px;
    background: var(--paper);
    color: var(--ink);
    overflow: hidden;
  }
  .rewards-name {
    position: absolute; top: 52px; left: 0; width: 100%;
    text-align: center;
    font-family: "Oswald", sans-serif; font-weight: 500;
    font-size: 24px; line-height: 1; letter-spacing: 1px;
    color: var(--ink);
  }
  .rewards-name .mark {
    display: inline-block; width: 12px; height: 12px;
    background: var(--accent-red); margin-right: 8px; vertical-align: 3px;
  }
  .headline {
    position: absolute; top: 130px; left: 94px; width: 382px; height: 92px;
    display: flex; align-items: stretch;
    font-family: "Oswald", sans-serif; font-weight: 400;
    font-size: 100px; line-height: 1;
  }
  .headline .plain {
    width: 161px; display: flex; align-items: center; justify-content: flex-start;
    letter-spacing: -1px;
  }
  .headline .boxed {
    width: 221px; background: var(--ink); color: var(--paper);
    border: 3px solid var(--ink);
    box-shadow: inset 0 0 0 2px var(--paper);
    display: flex; align-items: center; justify-content: center;
    letter-spacing: -2px; overflow: hidden;
  }
  .headline .word { display: inline-block; transform: scaleY(1.12); }
  .sale-word {
    position: absolute; top: 227px; left: 96px; width: 380px;
    display: flex; justify-content: space-between;
    font-family: "Oswald", sans-serif; font-weight: 400;
    font-size: 108px; line-height: 94px;
  }
  .flat-row {
    position: absolute; top: 351px; left: 94px; width: 382px;
    display: flex; align-items: center; gap: 14px;
    font-family: "Oswald", sans-serif; font-weight: 400;
    font-size: 62px; line-height: 60px;
  }
  .flat-row .rule { flex: 1; height: 2px; background: var(--ink); }
  .discount {
    position: absolute; top: 418px; left: 0; width: 100%;
    text-align: center;
    font-family: "Montserrat", sans-serif; font-weight: 800;
    font-size: 82px; line-height: 84px; letter-spacing: -1px;
  }
  .discount-note {
    position: absolute; top: 497px; left: 0; width: 100%;
    text-align: center;
    font-family: "Montserrat", sans-serif; font-weight: 700;
    font-size: 37px; line-height: 42px;
  }
  .code-band {
    position: absolute; top: 579px; left: 0; width: 100%; height: 41px;
    background: var(--accent-red); color: var(--light-text);
    display: flex; align-items: center; justify-content: center;
    font-family: "Open Sans", sans-serif; font-weight: 400;
    font-size: 27px;
  }
  .brand-name {
    position: absolute; top: 672px; left: 0; width: 100%;
    text-align: center;
    font-family: "Montserrat", sans-serif; font-weight: 800;
    font-size: 26px; line-height: 1; color: var(--accent-red);
  }
  .site-footer {
    position: absolute; left: 0; bottom: 0; width: 100%; height: 44px;
    background: var(--footer-bg); color: var(--light-text);
    display: flex; align-items: center; justify-content: center; gap: 12px;
    font-family: "Open Sans", sans-serif; font-size: 16px;
  }
  .site-footer svg { width: 18px; height: 18px; }
</style>
</head>
<body>
  <main class="flyer">
    <div class="rewards-name"><span class="mark"></span>RESONANT REWARDS</div>

    <h1 class="headline"><span class="plain"><span class="word">SUR</span></span><span class="boxed"><span class="word">PRICE</span></span></h1>
    <div class="sale-word"><span>S</span><span>A</span><span>L</span><span>E</span></div>

    <div class="flat-row"><span class="rule"></span><span>FLAT</span><span class="rule"></span></div>
    <p class="discount">20% OFF</p>
    <p class="discount-note">FOR FIRST ORDER</p>

    <div class="code-band">USE THE CODE : XYZ</div>

    <div class="brand-name">HARBOURLINE GUITARS</div>

    <footer class="site-footer">
      <svg viewBox="0 0 20 20" aria-hidden="true">
        <circle cx="10" cy="10" r="9" fill="none" stroke="#fff" stroke-width="1.6"/>
        <ellipse cx="10" cy="10" rx="4" ry="9" fill="none" stroke="#fff" stroke-width="1.4"/>
        <line x1="1" y1="10" x2="19" y2="10" stroke="#fff" stroke-width="1.4"/>
      </svg>
      <span>www.harbourlineguitars.co.uk/resonant-rewards</span>
    </footer>
  </main>
</body>
</html>
```